Therapy Dog Organization Website

Looking for a website that is user friendly, welcoming, dog themed and has the following pages and links:
*Click here to join - links to a jot form
*Click here to donate - links to our paypal page
*Request a visit - links to a jot form
*Facebook Follow Link
*Instagram Follow Link
*Our team - images uploaded to showcase our dogs
*Donors and Referrals Page - Where I can update as donations and referrals come in.
*Online store. Currently this is in Jot Form but I would like a store front. I would not want this to be a link but rather a hidden page, something like www.hollowbirch.org/teamstore.

Please visit www.hollowbirch.org to see what we have right now designed simply in Canva. Dog photos can be provided to use in images.

Note: I have funds from a grant that I have to spend to add gratuity to the project winner.

```html
<!DOCTYPE html>
<html lang="en">
<head>
<meta charset="utf-8">
<title>Hollow Birch Therapy Dogs</title>
<link href="https://fonts.googleapis.com/css2?family=Baloo+2:wght@600;700;800&family=DM+Sans:wght@400;500;700&display=swap" rel="stylesheet">
<style>
:root{
  --dark:#1f1d1b;
  --ink:#161412;
  --cream:#fffcf3;
  --sand:#fff4d6;
  --orange:#ff6b35;
  --yellow:#ffd23f;
  --teal:#5fd3dc;
  --green:#8fdc8a;
  --sky:#dcf1f4;
  --muted:#5d5850;
}
*{box-sizing:border-box;margin:0;padding:0}
html,body{width:1200px;height:5159px;overflow:hidden}
body{font-family:"DM Sans",sans-serif;color:var(--ink);background:var(--cream);position:relative}
h1,h2,h3{font-family:"Baloo 2",sans-serif}
.section{position:absolute;left:0;width:1200px}
.pill{display:inline-block;font-size:8px;font-weight:700;letter-spacing:.8px;text-transform:uppercase;border:1.5px solid var(--ink);border-radius:20px;padding:3px 10px;background:var(--cream)}
.btn{display:inline-block;font-size:10px;font-weight:700;border:2px solid var(--ink);border-radius:6px;padding:9px 18px;box-shadow:3px 3px 0 var(--ink);color:var(--ink);text-decoration:none}
.social{width:26px;height:26px;border-radius:50%;border:2px solid currentColor;display:inline-flex;align-items:center;justify-content:center}
.social span{width:8px;height:8px;border-radius:50%;background:currentColor}
.center{text-align:center}

.hero{top:0;height:668px;background:var(--dark);color:#fff}
.nav{position:absolute;top:20px;left:220px;right:220px;height:44px;display:flex;align-items:center}
.brand{display:flex;align-items:center;gap:8px;font-family:"Baloo 2",sans-serif;font-weight:700;font-size:19px;line-height:1}
.brand i{width:22px;height:22px;border-radius:50%;background:var(--cream);display:block}
.nav ul{list-style:none;display:flex;gap:22px;margin-left:70px;font-size:8.5px;font-weight:700;letter-spacing:.6px}
.nav .actions{margin-left:auto;display:flex;gap:10px}
.nav .btn{font-size:8px;padding:6px 12px;box-shadow:none}
.hero .kicker{position:absolute;left:220px;top:150px;background:var(--yellow);color:var(--ink);transform:rotate(-3deg)}
.hero h1{position:absolute;left:218px;top:178px;font-size:32px;line-height:36px;font-weight:800;white-space:nowrap}
.hero h1 span{display:block}
.hero h1 em{font-style:normal;color:var(--orange)}
.hero .lede{position:absolute;left:220px;top:306px;width:330px;font-size:12px;line-height:18px;color:#d8d2c6}
.hero .cta{position:absolute;left:220px;top:368px;display:flex;gap:14px}
.hero .donate{position:absolute;left:220px;top:413px;background:#fff;box-shadow:3px 3px 0 #fff;outline:2px solid #fff}
.hero .follow{position:absolute;left:220px;top:474px;display:flex;align-items:center;gap:10px;font-size:7px;color:#cfc8bb}
.hero .follow .social{color:#fff}
.hero-photo{position:absolute;left:620px;top:100px;width:360px;height:455px;transform:rotate(2.5deg);border:4px solid #fff;border-radius:12px;box-shadow:6px 6px 0 var(--orange);background:linear-gradient(160deg,#8ea0b7,#c8cdd4 45%,#c4a67a)}
.hero-badge{position:absolute;left:604px;top:530px;background:var(--yellow);color:var(--ink);font-size:10px;font-weight:700;padding:6px 12px;border:2px solid var(--ink);border-radius:20px;transform:rotate(-6deg)}
.scroll{position:absolute;left:0;right:0;top:582px;text-align:center;font-size:7px;letter-spacing:1px;color:#aaa}

.band{top:668px;height:36px;background:var(--yellow);display:flex;justify-content:center;align-items:center;gap:28px;font-size:8px;font-weight:700;letter-spacing:.5px;border-top:2px solid var(--ink);border-bottom:2px solid var(--ink)}
.band span::before{content:"";display:inline-block;width:7px;height:7px;background:var(--orange);border-radius:50%;margin-right:5px;vertical-align:middle}

.story{top:704px;height:592px;background:var(--cream)}
.story-photo{position:absolute;left:212px;top:775px;width:376px;height:450px;transform:rotate(-2deg);background:linear-gradient(180deg,#3a6fc8,#8aa8d8 45%,#6c6f76);border:6px solid #fff;outline:3px solid var(--ink);border-radius:8px;box-shadow:6px 6px 0 var(--ink)}
.story-badge{position:absolute;left:452px;top:1190px;background:var(--teal);border:2px solid var(--ink);border-radius:8px;padding:6px 12px;font-size:9px;font-weight:700;box-shadow:3px 3px 0 var(--ink)}
.story-badge small{display:block;font-weight:400;font-size:8px}
.story-copy{position:absolute;left:616px;top:866px;width:366px}
.story-copy .pill{background:var(--orange);color:#fff}
.story-copy h2{font-size:22px;font-weight:800;margin:10px 0 10px}
.story-copy p{font-size:10.5px;line-height:17px;color:var(--muted);margin-bottom:12px}
.story-copy a{font-size:9px;font-weight:700;color:var(--orange)}

.mission{top:1296px;height:464px;background:var(--sand);border-top:2px solid var(--ink);border-bottom:2px solid var(--ink)}
.mission .head{position:absolute;top:72px;left:0;right:0}
.mission h2{font-size:21px;font-weight:800;margin-top:8px}
.card{position:absolute;background:#fff;border:2px solid var(--ink);border-radius:10px;box-shadow:5px 5px 0 var(--ink);padding:28px 26px}
.card .icon{width:32px;height:32px;border:2px solid var(--ink);border-radius:6px;margin-bottom:16px}
.card h3{font-size:14px;font-weight:800;margin-bottom:10px}
.card p{font-size:9.5px;line-height:16px;color:var(--muted)}

.about{top:1760px;height:826px;background:var(--cream)}
.about .head{position:absolute;top:70px;left:0;right:0}
.about .pill{background:var(--green)}
.about h2{font-size:21px;font-weight:800;margin:6px 0 6px}
.about .head p{font-size:11px;line-height:17px;color:var(--muted);width:420px;margin:0 auto}
.tile{position:absolute;width:176px;height:136px;border:3px solid var(--ink);border-radius:6px;box-shadow:4px 4px 0 var(--ink);background:#fff;padding:4px}
.tile div{width:100%;height:100%;border-radius:3px}
.tile b{position:absolute;left:50%;bottom:-14px;transform:translateX(-50%);white-space:nowrap;font-size:7px;letter-spacing:.3px;text-transform:uppercase;border:1.5px solid var(--ink);border-radius:10px;padding:3px 8px}

.team{top:2586px;height:1034px;background:var(--dark);color:#fff}
.team .head{position:absolute;top:72px;left:0;right:0}
.team .pill{color:var(--ink)}
.team h2{font-size:22px;font-weight:800;margin:6px 0 6px}
.team .head p{font-size:11px;line-height:17px;color:#cfc8bb;width:400px;margin:0 auto}
.dog{position:absolute;width:146px;height:188px;border:5px solid;border-radius:8px;background:var(--cream);padding:6px}
.dog div{width:100%;height:100%;border-radius:4px}
.dog b{position:absolute;left:0;right:0;bottom:-22px;text-align:center;font-size:9px;font-weight:700;color:#fff}
.team .join{position:absolute;left:478px;top:928px;background:var(--yellow)}

.donors{top:3620px;height:582px;background:var(--sky)}
.donors .head{position:absolute;top:72px;left:0;right:0}
.donors .pill{background:#fff}
.donors h2{font-size:21px;font-weight:800;margin:6px 0 8px}
.donors .head p{font-size:11px;line-height:17px;color:var(--muted);width:440px;margin:0 auto}
.dcard{position:absolute;top:252px;width:238px;height:236px;background:#fff;border:2px solid var(--ink);border-radius:8px;box-shadow:5px 5px 0 var(--ink);padding:22px 18px;font-size:9px;color:var(--muted)}
.dcard h3{font-size:11px;font-weight:800;color:var(--ink);margin-bottom:14px;display:flex;align-items:center;gap:6px}
.dcard h3 i{width:9px;height:9px;border-radius:2px;display:block}
.dcard strong{display:block;color:var(--ink);font-size:9.5px;margin-bottom:3px}
.dcard .note{font-size:8px;line-height:12px;margin-bottom:14px}
.dcard ul{list-style:none}
.dcard li{margin-bottom:9px}
.dcard li::before{content:"";display:inline-block;width:5px;height:5px;background:var(--orange);border-radius:50%;margin-right:7px;vertical-align:middle}
.donors .foot{position:absolute;top:515px;left:0;right:0;font-size:9.5px;color:var(--muted)}
.donors .foot a{color:var(--orange)}

.ready{top:4202px;height:256px;background:var(--orange);color:#fff;border-top:2px solid var(--ink);border-bottom:2px solid var(--ink)}
.ready h2{position:absolute;top:60px;left:0;right:0;font-size:22px;font-weight:800}
.ready p{position:absolute;top:102px;left:0;right:0;font-size:11px;line-height:17px;color:#ffe6dc}
.ready p span{display:block}
.ready .row{position:absolute;top:160px;left:0;right:0;display:flex;justify-content:center;gap:10px}

.contact{top:4458px;height:430px;background:var(--cream)}
.contact .box{position:absolute;left:220px;top:70px;width:760px;height:296px;background:var(--dark);border-radius:12px;box-shadow:6px 6px 0 var(--teal);color:#fff;text-align:center;padding-top:46px}
.contact .pill{background:var(--dark);color:#fff;border-color:#fff}
.contact h2{font-size:22px;font-weight:800;margin:6px 0 6px}
.contact p{font-size:10.5px;line-height:16px;color:#cfc8bb;width:380px;margin:0 auto 16px}
.contact .btn{background:var(--orange);color:#fff;border-color:#fff;box-shadow:none}
.contact .socials{margin-top:18px;display:flex;justify-content:center;gap:12px;color:#fff}

.footer{top:4888px;height:271px;background:var(--dark);color:#cfc8bb}
.footer .brand{position:absolute;left:220px;top:48px;color:#fff;font-size:15px}
.footer .about-text{position:absolute;left:220px;top:100px;width:250px;font-size:9.5px;line-height:15px}
.footer .socials{position:absolute;left:220px;top:160px;display:flex;gap:8px;color:#fff}
.footer .socials .social{width:22px;height:22px}
.fcol{position:absolute;top:56px;font-size:9px;line-height:22px}
.fcol h4{font-size:8px;color:#fff;letter-spacing:1px;font-weight:700;margin-bottom:2px}
.footer .legal{position:absolute;left:220px;right:220px;top:240px;border-top:1px solid #3a3733;padding-top:10px;display:flex;justify-content:space-between;font-size:8px;color:#8f897e}
</style>
</head>
<body>

<section class="section hero">
  <nav class="nav">
    <div class="brand"><i></i>Hollow Birch</div>
    <ul><li>OUR STORY</li><li>MISSION</li><li>WHAT WE DO</li><li>OUR TEAM</li><li>DONORS</li><li>CONTACT</li></ul>
    <div class="actions">
      <a class="btn" style="color:#fff;border-color:#fff">Join Our Pack</a>
      <a class="btn" style="background:var(--orange);color:#fff;border-color:var(--orange)">Donate</a>
    </div>
  </nav>
  <span class="pill kicker">★ A Michigan Nonprofit</span>
  <h1><span>Bringing comfort, joy</span><span>&amp; unconditional love</span><span><em>— one paw at a time.</em></span></h1>
  <p class="lede">A Michigan nonprofit dedicated to providing therapy dogs to the community to spread joy, hope and healing.</p>
  <div class="cta">
    <a class="btn" style="background:var(--orange);color:#fff">Request a Visit →</a>
    <a class="btn" style="background:var(--teal)">Click Here to Join!</a>
  </div>
  <a class="btn donate">Click Here to Donate!</a>
  <div class="follow">Follow the Pack: <span class="social"><span></span></span><span class="social"><span></span></span></div>
  <div class="hero-photo" role="img" aria-label="Photo of a team mascot standing beside a therapy dog in a school gym"></div>
  <div class="hero-badge">15+ Pack Members!</div>
  <div class="scroll">SCROLL<br>⌄</div>
</section>

<div class="section band">
  <span>HOSPITALS</span><span>SCHOOLS</span><span>SENIOR COMMUNITIES</span><span>CERTIFIED THERAPY TEAMS</span><span>MICHIGAN NONPROFIT</span>
</div>

<section class="section story"></section>
<div class="story-photo" role="img" aria-label="Photo of two golden retrievers seated beside a blue event table"></div>
<div class="story-badge">15+ Pack Members<small>certified &amp; growing</small></div>
<div class="story-copy">
  <span class="pill">Our Story</span>
  <h2>Every wag tells a story.</h2>
  <p>Ours began with a simple belief: the love of a dog can change lives. What started with a few volunteers and their dogs has grown into a community dedicated to bringing comfort and joy wherever it's needed most.</p>
  <p>From hospitals to schools and senior centers, our therapy dog teams share moments of connection, calm, and healing — one visit at a time. At the heart of our mission is a simple truth: sometimes the best kind of therapy comes with four paws and a wagging tail.</p>
  <a>Read our mission &amp; purpose →</a>
</div>

<section class="section mission">
  <div class="head center"><span class="pill">Why We're Here</span><h2>Our mission &amp; purpose</h2></div>
  <div class="card" style="left:220px;top:166px;width:368px;height:230px;transform:rotate(-1deg)">
    <div class="icon" style="background:var(--orange)"></div>
    <h3>Our Mission</h3>
    <p>To certify and deploy therapy dog teams that promote emotional well-being, reduce stress, and foster empathy. We are dedicated to improving quality of life by bringing the unconditional love and calming presence of therapy dogs to those in need, while upholding the highest standards of animal welfare, professionalism, and community service.</p>
  </div>
  <div class="card" style="left:612px;top:166px;width:368px;height:230px;transform:rotate(1deg)">
    <div class="icon" style="background:var(--yellow)"></div>
    <h3>Our Purpose</h3>
    <p>Our purpose is to share the comfort, joy, and healing power of the human-animal bond. We connect trained therapy dog teams with people in need of emotional support, companionship, and encouragement in hospitals, schools, senior communities, and beyond — lifting spirits and easing stress, one visit at a time.</p>
  </div>
</section>

<section class="section about">
  <div class="head center"><span class="pill">Out &amp; About</span><h2>Spreading joy across our community</h2><p>From classrooms to courtside, our pack shows up wherever a wagging tail can make someone's day.</p></div>
  <div class="tile" style="left:220px;top:206px"><div role="img" aria-label="Photo collage of classroom visits" style="background:linear-gradient(135deg,#6d6460,#b8aca3)"></div><b style="background:var(--orange)">Classroom Visits</b></div>
  <div class="tile" style="left:414px;top:206px"><div role="img" aria-label="Photo of a therapy dog at a game day" style="background:linear-gradient(135deg,#4a7ad0,#d7c7a3)"></div><b style="background:var(--teal)">Game-Day Visits</b></div>
  <div class="tile" style="left:608px;top:206px"><div role="img" aria-label="Photo of dogs visiting first responders outdoors" style="background:linear-gradient(135deg,#8ea16a,#c9c3b0)"></div><b style="background:var(--yellow)">First Responders</b></div>
  <div class="tile" style="left:802px;top:206px"><div role="img" aria-label="Photo of the pack gathered together indoors" style="background:linear-gradient(135deg,#cfc9bf,#9a8a6e)"></div><b style="background:var(--green)">The Pack, Together</b></div>

  <div class="tile" style="left:220px;top:398px"><div role="img" aria-label="Photo of a therapy dog at a school event" style="background:linear-gradient(135deg,#2f5fb8,#30302f)"></div><b style="background:var(--orange)">School &amp; Event Visits</b></div>
  <div class="tile" style="left:414px;top:398px"><div role="img" aria-label="Photo of a dog in a vest at a meet and greet" style="background:linear-gradient(135deg,#3b3b3b,#59c2cf)"></div><b style="background:var(--teal)">Meet &amp; Greet Moments</b></div>
  <div class="tile" style="left:608px;top:398px"><div role="img" aria-label="Photo of vested dogs sitting in a row" style="background:linear-gradient(135deg,#c25a4a,#d8c9b0)"></div><b style="background:var(--yellow)">Vested &amp; Ready</b></div>
  <div class="tile" style="left:802px;top:398px"><div role="img" aria-label="Photo of an energetic dog with visitors" style="background:linear-gradient(135deg,#7c8aa0,#c2b3a0)"></div><b style="background:var(--green)">Full of Energy</b></div>

  <div class="tile" style="left:220px;top:590px"><div role="img" aria-label="Photo of a dog beside a classic car at a show" style="background:linear-gradient(135deg,#6e8fa8,#2c2c2c)"></div><b style="background:var(--orange)">Community &amp; Car Shows</b></div>
  <div class="tile" style="left:414px;top:590px"><div role="img" aria-label="Photo of dogs at a senior community visit" style="background:linear-gradient(135deg,#5a4030,#a07850)"></div><b style="background:var(--teal)">Senior Community Visits</b></div>
  <div class="tile" style="left:608px;top:590px"><div role="img" aria-label="Photo of a handler with her dog" style="background:linear-gradient(135deg,#4b4f6b,#b5adc0)"></div><b style="background:var(--yellow)">Handlers &amp; Their Pups</b></div>
  <div class="tile" style="left:802px;top:590px"><div role="img" aria-label="Photo of a dog beside a holiday tree at a hospital" style="background:linear-gradient(135deg,#d8d4ce,#2e6b6a)"></div><b style="background:var(--green)">Holiday Hospital Visits</b></div>
</section>

<section class="section team">
  <div class="head center"><span class="pill">Meet the Pack</span><h2>Our Team</h2><p>Every member of our pack is a certified therapy dog with a heart for helping others. Say hello to a few of our good boys and girls!</p></div>

  <div class="dog" style="left:220px;top:210px;border-color:var(--orange)"><div role="img" aria-label="Portrait card of Juniper, a black fluffy dog" style="background:linear-gradient(180deg,#8fb7d8,#2a2a2a)"></div><b>Juniper</b></div>
  <div class="dog" style="left:379px;top:210px;border-color:var(--teal)"><div role="img" aria-label="Portrait card of Biscuit, a brown dog" style="background:linear-gradient(180deg,#8fb7d8,#8a6642)"></div><b>Biscuit</b></div>
  <div class="dog" style="left:538px;top:210px;border-color:var(--yellow)"><div role="img" aria-label="Portrait card of Pepper, a black and white dog" style="background:linear-gradient(180deg,#8fb7d8,#33373b)"></div><b>Pepper</b></div>
  <div class="dog" style="left:697px;top:210px;border-color:var(--green)"><div role="img" aria-label="Portrait card of Clover, a small fluffy dog" style="background:linear-gradient(180deg,#8fb7d8,#d8a56a)"></div><b>Clover</b></div>
  <div class="dog" style="left:856px;top:210px;border-color:var(--orange)"><div role="img" aria-label="Portrait card of Hank, a grey and white dog" style="background:linear-gradient(180deg,#8fb7d8,#6f6a66)"></div><b>Hank</b></div>

  <div class="dog" style="left:220px;top:448px;border-color:var(--teal)"><div role="img" aria-label="Portrait card of Willow, a long-haired tan dog" style="background:linear-gradient(180deg,#8fb7d8,#b08758)"></div><b>Willow</b></div>
  <div class="dog" style="left:379px;top:448px;border-color:var(--yellow)"><div role="img" aria-label="Portrait card of Marigold, a golden doodle" style="background:linear-gradient(180deg,#8fb7d8,#d6b07c)"></div><b>Marigold</b></div>
  <div class="dog" style="left:538px;top:448px;border-color:var(--orange)"><div role="img" aria-label="Portrait card of Honey, a golden dog" style="background:linear-gradient(180deg,#8fb7d8,#d9b274)"></div><b>Honey</b></div>
  <div class="dog" style="left:697px;top:448px;border-color:var(--teal)"><div role="img" aria-label="Portrait card of Ollie, a white dog" style="background:linear-gradient(180deg,#8fb7d8,#e8e4dc)"></div><b>Ollie</b></div>
  <div class="dog" style="left:856px;top:448px;border-color:var(--green)"><div role="img" aria-label="Portrait card of Bruno, a curly brown dog" style="background:linear-gradient(180deg,#8fb7d8,#9a6a45)"></div><b>Bruno</b></div>

  <div class="dog" style="left:220px;top:686px;border-color:var(--yellow)"><div role="img" aria-label="Portrait card of Daisy, a white fluffy dog" style="background:linear-gradient(180deg,#8fb7d8,#efe9dd)"></div><b>Daisy</b></div>
  <div class="dog" style="left:379px;top:686px;border-color:var(--green)"><div role="img" aria-label="Portrait card of Nutmeg, a small tan and white dog" style="background:linear-gradient(180deg,#8fb7d8,#c99f74)"></div><b>Nutmeg</b></div>
  <div class="dog" style="left:538px;top:686px;border-color:var(--orange)"><div role="img" aria-label="Portrait card of Scout, a tan dog" style="background:linear-gradient(180deg,#8fb7d8,#b98d55)"></div><b>Scout</b></div>
  <div class="dog" style="left:697px;top:686px;border-color:var(--teal)"><div role="img" aria-label="Portrait card of Maple, a cream puppy" style="background:linear-gradient(180deg,#8fb7d8,#ece2cf)"></div><b>Maple</b></div>
  <div class="dog" style="left:856px;top:686px;border-color:var(--yellow)"><div role="img" aria-label="Portrait card of Cocoa, a chocolate dog" style="background:linear-gradient(180deg,#c8a8d8,#6a4838)"></div><b>Cocoa</b></div>

  <a class="btn join">Think your pup has what it takes? Join the pack</a>
</section>

<section class="section donors">
  <div class="head center"><span class="pill">With Gratitude</span><h2>Donors &amp; Referrals</h2><p>Our donors and referral partners are the heart of our organization. Because of their generosity, we're able to keep costs low for our therapy dog teams while never compromising the integrity, training, and care of our handlers and dogs. Thank you for believing in our mission and helping us spread healing one paw at a time.</p></div>
  <div class="dcard" style="left:222px;transform:rotate(-1deg)">
    <h3><i style="background:var(--teal)"></i>Corporate Donors</h3>
    <strong>Brightline Tech</strong>
    <div class="note">Cloud phone systems built for reliable business communications.</div>
    <strong>Maple Ridge Post 21, Veterans Hall</strong>
    <div class="note">Serving veterans from the local community since 1950. To all who have served — thank you!</div>
  </div>
  <div class="dcard" style="left:482px">
    <h3><i style="background:var(--yellow)"></i>Individual Donors</h3>
    <ul><li>Doris Lane</li><li>Carl Whitford</li><li>Roy Lane</li><li>Nora Pruitt</li><li>Tessa Ellwood</li><li>Jonah Lane</li><li>Reid Marsh</li></ul>
  </div>
  <div class="dcard" style="left:742px;transform:rotate(1deg)">
    <h3><i style="background:var(--orange)"></i>Referrals</h3>
    <strong>Steadfast Canine Training</strong>
    <div class="note">Northern Michigan dog training facility — bridging the communication gap between dogs &amp; owners.</div>
  </div>
  <p class="foot center">Want to support our pack? <a>Click here to donate</a> or <a>contact us</a> about becoming a referral partner.</p>
</section>

<section class="section ready center">
  <h2>Ready to spread some joy?</h2>
  <p><span>Whether you'd love a visit, want to join our pack with your pup, or simply want to</span><span>help us keep going — there's a place for you here.</span></p>
  <div class="row">
    <a class="btn" style="background:#fff">Request a Visit</a>
    <a class="btn" style="background:var(--yellow)">Click Here to Join!</a>
    <a class="btn" style="background:var(--orange);color:#fff">Click Here to Donate!</a>
  </div>
</section>

<section class="section contact">
  <div class="box">
    <span class="pill">Get In Touch</span>
    <h2>Contact Us</h2>
    <p>Have a question about scheduling a visit, joining the pack, or partnering with Hollow Birch? We'd love to hear from you.</p>
    <a class="btn">Please Click Here to Contact Us →</a>
    <div class="socials"><span class="social"><span></span></span><span class="social"><span></span></span></div>
  </div>
</section>

<footer class="section footer">
  <div class="brand"><i></i>Hollow Birch</div>
  <p class="about-text">A Michigan nonprofit dedicated to providing therapy dogs to the community to spread joy, hope and healing — one paw at a time.</p>
  <div class="socials"><span class="social"><span></span></span><span class="social"><span></span></span></div>
  <div class="fcol" style="left:612px"><h4>EXPLORE</h4>Our Story<br>Mission &amp; Purpose<br>What We Do<br>Our Team<br>Donors &amp; Referrals</div>
  <div class="fcol" style="left:808px"><h4>GET INVOLVED</h4>Join Our Pack<br>Request a Visit<br>Donate<br>Contact Us</div>
  <div class="legal"><span>© 2026 Hollow Birch Therapy Dogs. A Michigan nonprofit. All rights reserved.</span><span>Made with ♥ for people &amp; pups alike.</span></div>
</footer>

</body>
</html>
```